Corporate Web Redesign Project - coded

We would like redesign/refresh of our current site that would allow us to increase the depth of content and create a high quality impression for visitors.

Current site - http://corvanisystems.com/

A previous web redesign project has improved our site but it has not really reached the level we require.

Our customers are global, blue chip, organisations and a professional, corporate style of site is required.

Please note we would prefer a coded website to a just a design. We are happy to provide a zip of our current site if required.
Updates

                                   

Target Market(s)

Global oil and gas producers, KR, Tamberline, Orvadex etc.

Industry/Entity Type

It Professional

Requirements
Must have
• Design should support the level of content we currently have in the existing sitemap - although it should be expandable a site design for a large / complex site would not be appropriate

All current content / pages to be reflected in design

Must be visually appealing

Intuitive and clear navigation that is expandable

Display a high level of professionalism

Use a consistent palette of colours that complements our logo

Clean and organized layout

A way to capture visitor’s information or Call to action (i.e. contact link or form) on every page

Prominent Contact Information
Should not have
• Flash

```html
<!DOCTYPE html>
<html lang="en">
<head>
<meta charset="utf-8">
<title>Corvani Systems</title>
<link href="https://fonts.googleapis.com/css2?family=Ubuntu:wght@300;400;500;700&family=Arimo:wght@400;700&display=swap" rel="stylesheet">
<style>
:root{
  --olive:#8a9456;
  --olive-dark:#6f7a40;
  --teal:#1f4a5e;
  --teal-text:#1d4a5c;
  --link:#1a6f9a;
  --text:#333;
  --muted:#666;
  --address:#5f6d1f;
  --panel:#eaf1f4;
  --line:#c9d1d4;
}
*{margin:0;padding:0;box-sizing:border-box}
html,body{width:960px;height:1200px;overflow:hidden}
body{position:relative;background:#fff;font-family:"Arimo",Arial,sans-serif;color:var(--text)}
.abs{position:absolute}
.top-band{left:0;top:0;width:960px;height:506px;background:linear-gradient(#fff 0%,#eef3f5 30%,#b9cdd5 100%)}
.brand{left:81px;top:30px;display:flex;align-items:center;gap:8px;font-family:"Ubuntu",sans-serif;font-weight:500;font-size:22px;color:var(--teal)}
.brand .mark{width:30px;height:30px;border-radius:50%;background:var(--teal)}
.top-links{left:768px;top:18px;font-family:"Ubuntu",sans-serif;font-size:10px;color:#777;letter-spacing:.3px}
.top-links span{margin:0 8px}
.social{top:43px;width:30px;height:30px;border-radius:50%;background:#7e98a6}
.nav{left:81px;top:86px;width:799px;height:32px;background:linear-gradient(#9aa463,#6f7a40);border-radius:5px 5px 6px 6px;box-shadow:0 2px 3px rgba(0,0,0,.25);overflow:hidden}
.nav a{position:absolute;top:0;line-height:32px;color:#fff;font-family:"Ubuntu",sans-serif;font-size:13px;letter-spacing:.5px;text-decoration:none;transform:translateX(-50%)}
.nav .div{position:absolute;top:0;width:1px;height:32px;background:rgba(255,255,255,.35)}
.call{position:absolute;right:0;top:0;width:190px;height:32px;background:var(--teal);clip-path:polygon(18px 0,100% 0,100% 100%,0 100%);color:#fff;font-size:11.5px;line-height:32px;padding-left:29px}
.hero{left:81px;top:132px;width:797px;height:352px;background:#fff;border-radius:5px;padding:3px;box-shadow:0 6px 10px rgba(0,0,0,.2)}
.hero-img{width:100%;height:100%;border-radius:3px;background:linear-gradient(#6f90c2 0%,#9db5d5 55%,#e0c391 76%,#e6a965 100%)}
.hero-panel{left:102px;top:202px;width:336px;height:189px;background:rgba(70,100,125,.72);border-radius:4px;color:#fff;padding:16px 0 0 8px}
.hero-panel h1{font-family:"Ubuntu",sans-serif;font-weight:300;font-size:23px;margin-bottom:16px}
.hero-panel ul{list-style:none;padding-left:18px;font-size:11.5px}
.hero-panel li{position:relative;margin-bottom:15px;width:270px;line-height:1.25}
.hero-panel li::before{content:"";position:absolute;left:-13px;top:5px;width:4px;height:4px;background:#fff}
.card{top:522px;width:186px;height:180px;border:1px solid var(--line);border-radius:4px;overflow:hidden}
.card h2{height:30px;background:var(--olive);color:#fff;font-family:"Ubuntu",sans-serif;font-weight:400;font-size:12.5px;line-height:30px;padding-left:10px;letter-spacing:.3px}
.card .pic{width:60px;height:64px;margin:6px auto 10px;border-radius:6px}
.card p{font-size:10.3px;line-height:1.25;padding:0 10px;text-align:justify;color:#111}
.card .more{position:absolute;right:10px;bottom:12px;font-size:10.5px;color:var(--address)}
.h3{font-family:"Ubuntu",sans-serif;font-size:13px;color:var(--teal-text);letter-spacing:.3px}
.about p{width:522px;font-size:11px;line-height:18px;color:#444;letter-spacing:.2px;margin-bottom:17px}
.offices{left:81px;top:858px;width:519px;height:132px;background:var(--panel);border:1px solid #dde6ea;border-radius:4px}
.office{top:8px;font-size:11px;line-height:17.6px;color:var(--address)}
.office h4{font-family:"Ubuntu",sans-serif;font-weight:400;font-size:13px;color:#222;margin-bottom:7px}
.office .mail{color:#111}
.offices .sep{left:265px;top:4px;width:1px;height:122px;background:var(--line)}
.news-item{left:636px;width:236px;height:62px}
.news-item .thumb{position:absolute;left:0;top:0;width:56px;height:46px;background:linear-gradient(#8aa0b6,#3f5f80)}
.news-item h5{position:absolute;left:68px;top:-2px;font-family:"Ubuntu",sans-serif;font-weight:400;font-size:11px;color:var(--link)}
.news-item .sum{position:absolute;left:67px;top:16px;width:170px;font-size:8.5px;line-height:13px;color:#666}
.news-item .date{position:absolute;left:0;top:54px;font-size:8.5px;color:var(--link)}
.news-item .more{position:absolute;right:0;top:54px;font-size:8.5px;color:#111}
.client{top:1030px;width:110px;text-align:center;font-family:"Ubuntu",sans-serif;font-weight:500;font-size:14px;color:#555}
.foot-strip{left:0;top:1090px;width:960px;height:9px;background:var(--olive)}
.footer{left:0;top:1099px;width:960px;height:101px;background:var(--teal);color:#fff}
.foot-brand{left:87px;top:25px;display:flex;align-items:center;gap:7px;font-family:"Ubuntu",sans-serif;font-weight:500;font-size:16px}
.foot-brand .mark{width:20px;height:20px;border-radius:50%;background:#fff}
.touch{left:338px;top:11px;width:250px;height:38px;border:2px solid #fff;border-radius:5px;display:flex;align-items:center;padding-left:13px;gap:10px}
.touch span{font-family:"Ubuntu",sans-serif;font-weight:700;font-size:20px}
.partner{left:695px;top:18px}
.partner b{display:block;font-family:"Ubuntu",sans-serif;font-weight:400;font-size:18px}
.partner small{font-size:7px;letter-spacing:.2px}
.copy{left:83px;top:82px;font-size:8.5px}
.legal{right:80px;top:82px;font-size:8.5px;word-spacing:10px}
</style>
</head>
<body>
<div class="abs top-band"></div>

<header>
  <div class="abs brand"><span class="mark"></span>Corvani Systems</div>
  <nav class="abs top-links">Home<span>|</span>Contact Us</nav>
  <div class="abs social" style="left:771px" role="img" aria-label="Social network link"></div>
  <div class="abs social" style="left:809px" role="img" aria-label="Social network link"></div>
  <div class="abs social" style="left:845px" role="img" aria-label="News feed link"></div>
  <nav class="abs nav">
    <a href="#" style="left:56px">Home</a>
    <span class="div" style="left:111px"></span>
    <a href="#" style="left:157px">News</a>
    <span class="div" style="left:203px"></span>
    <a href="#" style="left:278px">About Us</a>
    <span class="div" style="left:336px"></span>
    <a href="#" style="left:405px">Solutions</a>
    <span class="div" style="left:469px"></span>
    <a href="#" style="left:533px">Contact Us</a>
    <div class="call">Call Now: +44(0)1224 480312</div>
  </nav>
</header>

<section class="abs hero">
  <div class="hero-img" role="img" aria-label="Drilling rig and storage tanks on desert sand under a blue sky"></div>
</section>
<div class="abs hero-panel">
  <h1>The Business of Drilling Wells</h1>
  <ul>
    <li>Understanding and communicating project cost and risk</li>
    <li>Control and reduce expenditure</li>
    <li>Learn and improve performance</li>
  </ul>
</div>

<section>
  <article class="abs card" style="left:81px">
    <h2>Time &amp; Cost Estimation</h2>
    <div class="pic" style="background:linear-gradient(#f3e6a0,#c9a84a)" role="img" aria-label="Folder with clock icon"></div>
    <p>PLX delivers a standardized, systematic approach to understanding project risk.</p>
    <span class="more">readmore...</span>
  </article>
  <article class="abs card" style="left:285px">
    <h2>Materials &amp; Cost Control</h2>
    <div class="pic" style="background:linear-gradient(90deg,#e0458a,#f0a030,#5ab84a,#3a8fd8)" role="img" aria-label="Colourful bar chart icon"></div>
    <p>MTX has been helping companies optimize materials and cost tracking processes since 1992.</p>
    <span class="more">readmore...</span>
  </article>
  <article class="abs card" style="left:489px">
    <h2>Lessons Learned</h2>
    <div class="pic" style="background:linear-gradient(90deg,#2f6a3a,#2b7fd0)" role="img" aria-label="Stack of books icon"></div>
    <p>LNX is an advanced lessons learned &amp; knowledge system for use in the energy industry.</p>
  </article>
  <article class="abs card" style="left:693px">
    <h2>Services &amp; Consulting</h2>
    <div class="pic" style="background:linear-gradient(#555,#222)" role="img" aria-label="Support consultant icon"></div>
    <p>Successful software implementations rely on people and processes to deliver results.</p>
  </article>
</section>

<section class="abs about" style="left:81px;top:725px">
  <h3 class="h3" style="margin-bottom:11px">About Us</h3>
  <p>From early phase evaluation through planning, execution and post analysis of wells, we deliver the tools, processes and people required to facilitate major performance improvement and cost savings.</p>
  <p>Our solutions are used in more than 30 countries to support operations ranging from a single well to global deployments with Major Operators.</p>
</section>

<section class="abs offices">
  <div class="abs office" style="left:48px">
    <h4>Europe</h4>
    18 Harlow Lane<br>Aberdeen<br>AB11 4QT<br>Phone:+44(0)1224 480312<br><span class="mail">Email: eu@corvanisystems.com</span>
  </div>
  <div class="abs sep"></div>
  <div class="abs office" style="left:308px">
    <h4>North America</h4>
    4100 Westfield Pkwy<br>Suite 210<br>Houston, TX 77063<br>Phone:(713) 555 0147<br><span class="mail">Email: us@corvanisystems.com</span>
  </div>
</section>

<section>
  <h3 class="abs h3" style="left:635px;top:724px">Latest News</h3>
  <div class="abs news-item" style="top:750px">
    <div class="thumb" role="img" aria-label="Pipeline valves photo"></div>
    <h5>PLX Selected by Brimwood</h5>
    <div class="sum">Eastfield Water Board is using Harlan Public Sector to</div>
    <div class="date">Posted on 02:00 PM on 24 Aug 2013</div><div class="more">more...</div>
  </div>
  <div class="abs news-item" style="top:829px">
    <div class="thumb" role="img" aria-label="Pipeline valves photo"></div>
    <div class="sum">Eastfield Water Board is using Harlan Public Sector to</div>
    <div class="date">Posted on 02:00 PM on 24 Aug 2013</div><div class="more">more...</div>
  </div>
  <div class="abs news-item" style="top:915px">
    <div class="thumb" role="img" aria-label="Pipeline valves photo"></div>
    <div class="sum">Eastfield Water Board is using Harlan Public Sector to</div>
    <div class="date">Posted on 02:00 PM on 24 Aug 2013</div><div class="more">more...</div>
  </div>
</section>

<section>
  <div class="abs client" style="left:57px">Orvadex</div>
  <div class="abs client" style="left:177px">Varno</div>
  <div class="abs client" style="left:299px">Keltra</div>
  <div class="abs client" style="left:420px">Brimwood</div>
  <div class="abs client" style="left:541px">KR</div>
  <div class="abs client" style="left:662px">Ostrel</div>
  <div class="abs client" style="left:783px">Dunmore</div>
</section>

<div class="abs foot-strip"></div>
<footer class="abs footer">
  <div class="abs foot-brand"><span class="mark"></span>Corvani Systems</div>
  <a class="abs touch" href="#" style="color:#fff;text-decoration:none">
    <span>Get In Touch</span>
    <svg width="22" height="22" viewBox="0 0 24 24" fill="#fff"><path d="M6.6 10.8a15 15 0 0 0 6.6 6.6l2.2-2.2c.3-.3.7-.4 1-.2 1.1.4 2.3.6 3.6.6.6 0 1 .4 1 1V20c0 .6-.4 1-1 1A17 17 0 0 1 3 4c0-.6.4-1 1-1h3.5c.6 0 1 .4 1 1 0 1.3.2 2.5.6 3.6.1.3 0 .7-.2 1z"/></svg>
    <svg width="22" height="18" viewBox="0 0 24 18" fill="none" stroke="#fff" stroke-width="2"><rect x="1" y="1" width="22" height="16" rx="1"/><path d="M1 1l11 9 11-9M1 17l8-7M23 17l-8-7"/></svg>
    <svg width="16" height="22" viewBox="0 0 16 22" fill="none" stroke="#fff" stroke-width="2"><path d="M8 21s7-8 7-13A7 7 0 0 0 1 8c0 5 7 13 7 13z"/><circle cx="8" cy="8" r="2.5"/></svg>
  </a>
  <div class="abs partner"><b>Cloudvane Partner</b><small>Gold Independent Software Vendor (ISV)</small></div>
  <div class="abs copy">Copyright © Corvani Systems Ltd 2013</div>
  <div class="abs legal">Privacy Legal Site&nbsp;map</div>
</footer>
</body>
</html>
```